Luminously Grounded Vitality

We want to design a business card that is modern and appealing for an innovative psychedelic telemedicine company that provides at-home ketamine-assisted therapy along with wellness, longevity, and anti-aging medicines. We want to use our deep purple and white plus other colors you can find on our website. We don't have any strict brand guidelines yet so feel free to get creative. We want a very professional, but technology first modern design that will instill trust, peace, calm, but also be attractive to investors in the healthcare and SaaS space.

```html
<!DOCTYPE html>
<html lang="en">
<head>
<meta charset="utf-8">
<title>Luminously – Business Card</title>
<link rel="stylesheet" href="https://fonts.googleapis.com/css2?family=Source+Sans+3:wght@300;400;600&family=Quicksand:wght@500;600&display=swap">
<style>
  :root {
    --backdrop: #5f4586;
    --card-white: #ffffff;
    --card-violet: #7d61ad;
    --violet-deep: #5d3f97;
    --violet-mark: #7e5cbb;
    --rose: #b2559f;
    --ink: #2a2433;
    --mist: #ebe6f4;
  }
  * { margin: 0; padding: 0; box-sizing: border-box; }
  html, body { width: 1200px; height: 781px; overflow: hidden; }
  body {
    background: var(--backdrop);
    font-family: "Source Sans 3", sans-serif;
    position: relative;
  }
  .card {
    position: absolute;
    top: 242px;
    width: 520px;
    height: 297px;
    border-radius: 18px;
    overflow: hidden;
  }
  .card--back { left: 50px; background: var(--card-violet); }
  .card--front { left: 630px; background: var(--card-white); }

  .back-wordmark {
    position: absolute;
    inset: 0;
    display: flex;
    align-items: center;
    justify-content: center;
    gap: 14px;
  }
  .back-wordmark .dot {
    width: 22px; height: 22px; border-radius: 50%;
    background: var(--violet-deep);
  }
  .back-wordmark .name {
    font-weight: 300;
    font-size: 46px;
    color: var(--violet-deep);
    letter-spacing: 0.5px;
  }

  .front-decor {
    position: absolute;
    right: -40px;
    bottom: -70px;
    width: 260px;
    height: 260px;
    border-radius: 50%;
    background: var(--mist);
  }
  .brand {
    position: absolute;
    left: 34px;
    top: 30px;
    display: flex;
    align-items: center;
    gap: 10px;
  }
  .brand .dot {
    width: 18px; height: 18px; border-radius: 50%;
    background: var(--violet-mark);
  }
  .brand .name {
    font-weight: 300;
    font-size: 34px;
    color: var(--rose);
  }
  .person {
    position: absolute;
    left: 34px;
    top: 120px;
  }
  .person .full-name {
    font-family: "Quicksand", sans-serif;
    font-weight: 600;
    font-size: 19px;
    color: var(--rose);
    letter-spacing: 0.5px;
  }
  .person .role {
    font-size: 12px;
    color: var(--ink);
    margin-top: 1px;
  }
  .contacts {
    position: absolute;
    left: 34px;
    top: 188px;
    list-style: none;
    font-family: "Quicksand", sans-serif;
    font-weight: 500;
    font-size: 12.5px;
    color: var(--ink);
  }
  .contacts li {
    display: flex;
    align-items: center;
    gap: 8px;
    height: 21px;
  }
  .contacts .phone { letter-spacing: 1.5px; }
  .contacts svg { width: 12px; height: 12px; flex: none; }
</style>
</head>
<body>

  <section class="card card--back" aria-label="Card back">
    <div class="back-wordmark">
      <span class="dot"></span>
      <span class="name">Luminously</span>
    </div>
  </section>

  <section class="card card--front" aria-label="Card front">
    <div class="front-decor" aria-hidden="true"></div>

    <div class="brand">
      <span class="dot"></span>
      <span class="name">Luminously</span>
    </div>

    <div class="person">
      <p class="full-name">Mara Ellison</p>
      <p class="role">Owner</p>
    </div>

    <ul class="contacts">
      <li class="phone">
        <svg viewBox="0 0 24 24" aria-hidden="true"><path fill="#7e5cbb" d="M6.6 10.8a15.1 15.1 0 0 0 6.6 6.6l2.2-2.2a1 1 0 0 1 1-.25 11.4 11.4 0 0 0 3.6.57 1 1 0 0 1 1 1V20a1 1 0 0 1-1 1A17 17 0 0 1 3 4a1 1 0 0 1 1-1h3.5a1 1 0 0 1 1 1c0 1.25.2 2.45.57 3.6a1 1 0 0 1-.25 1z"/></svg>
        (555) 014-2870
      </li>
      <li>
        <svg viewBox="0 0 24 24" aria-hidden="true"><rect x="2" y="5" width="20" height="14" rx="1.5" fill="#7e5cbb"/><path d="M3 6l9 7 9-7" fill="none" stroke="#fff" stroke-width="1.6"/></svg>
        info@luminously.example
      </li>
      <li>
        <svg viewBox="0 0 24 24" aria-hidden="true"><g fill="none" stroke="#7e5cbb" stroke-width="2"><circle cx="12" cy="12" r="9.5"/><ellipse cx="12" cy="12" rx="4" ry="9.5"/><path d="M2.5 12h19M4.5 7h15M4.5 17h15"/></g></svg>
        luminously.example
      </li>
    </ul>
  </section>

</body>
</html>
```